Free Printer Promotion

Hi i need a banner AD for my website.

The promotion is: free printer, for a monthly cost you get all the supplies and service included. Its a subscription service for printing. There is 5 plans available.
Prices vary upon printers, most expensive plan is $69.94 a month for a 1 year term and the most affordable plan is $9.95 a month for 3 year term

1 Monochrome laser (print only printer, black and white printing)
2 Multifunction Monochrome laser (print scan copy fax printer, black and white printing)

• Monochrome Printers are given 1000 prints per month
• Toner included
• Service included
• Printer included

3 Color laser (print only printer, color printing)
4 Multifunction Color laser (print scan copy fax, color printing)
Color printers are given 500 monochrome prints and 500 color prints per month
• Toner included
• Service included
• Printer included

5 Inkjet color printer (print copy scan fax, color printing)
• Inkjet Printers are given 1000 prints per month.
• Ink included
• Service included
• Printer included

Target Market(s)

students, home office workers, corporate business and government

Font styles to use
Serif
Sans Serif

Requirements
Must have
• i want it to be enticing, no long sentences. the customer will click on the banner and it will bring them to another page with the information.

Keep it short and sweet.

```html
<!DOCTYPE html>
<html lang="en">
<head>
<meta charset="utf-8">
<title>Free Printer Promotion</title>
<link href="https://fonts.googleapis.com/css2?family=Anton&family=Bebas+Neue&family=Roboto:wght@400;500&family=Roboto+Condensed:wght@400&display=swap" rel="stylesheet">
<style>
  :root {
    --night: #13163e;
    --navy: #141a4a;
    --blue: #3b7fc4;
    --blue-light: #6ea6dc;
    --teal: #006a8e;
    --teal-text: #0e6a8f;
    --mist: #e4eef2;
    --ink: #1b1f3a;
    --grey-bg: #e8e8e8;
    --white: #ffffff;
    --black: #000000;
  }
  * { box-sizing: border-box; margin: 0; padding: 0; }
  html, body { width: 925px; height: 1200px; overflow: hidden; }
  body {
    position: relative;
    font-family: "Roboto", Arial, sans-serif;
    background: linear-gradient(var(--night) 0 422px, var(--white) 422px 688px, var(--black) 688px);
  }
  .sprites { position: absolute; width: 0; height: 0; }

  /* Burst price badge */
  .badge { position: absolute; color: var(--white); text-align: center; }
  .badge svg { position: absolute; inset: 0; width: 100%; height: 100%; }
  .badge__text { position: absolute; inset: 0; display: flex; flex-direction: column; justify-content: center; align-items: center; line-height: 1.1; }
  .badge__price { font-weight: 500; }

  /* Web banners */
  .banner {
    position: absolute; left: 214px; width: 549px; height: 137px;
    background: linear-gradient(100deg, var(--blue) 40%, #2f6fb4 100%);
    border: 1px solid #0b0e2a; overflow: hidden;
  }
  .banner--fr { top: 65px; }
  .banner--en { top: 246px; }
  .banner__photo { position: absolute; left: 0; top: 0; width: 320px; height: 137px; }
  .banner__badge { left: 17px; top: 7px; width: 83px; height: 83px; }
  .banner__badge .badge__price { font-size: 16px; }
  .banner__badge .badge__line { font-size: 10.5px; }
  .banner__copy { position: absolute; left: 300px; width: 248px; top: 0; height: 137px; text-align: center; }
  .banner__title {
    font-family: "Anton", Impact, sans-serif; color: var(--white); font-weight: 400;
    text-shadow: 1px 2px 3px rgba(0,0,0,.45); letter-spacing: .2px;
  }
  .banner--fr .banner__title { font-size: 25px; margin-top: 14px; line-height: 1.2; }
  .banner--en .banner__title { font-size: 33px; margin-top: 10px; line-height: 1.05; }
  .banner__sub { color: var(--navy); line-height: 1.2; }
  .banner--fr .banner__sub { font-size: 11.5px; margin-top: 4px; }
  .banner--en .banner__sub { font-size: 13px; margin-top: 3px; }
  .pill {
    position: absolute; left: 28px; top: 94px; width: 197px; height: 28px;
    background: var(--navy); border-radius: 14px; color: var(--white);
    font-family: "Bebas Neue", Impact, sans-serif; font-size: 20px; line-height: 29px;
    box-shadow: 0 3px 5px rgba(0,0,0,.4); display: flex; justify-content: center; gap: 8px;
  }
  .pill svg { width: 9px; height: 13px; margin-top: 8px; }

  /* Flyers */
  .flyer {
    position: absolute; top: 458px; width: 345px; height: 687px;
    background: var(--white); border: 1px solid #222; overflow: hidden; color: var(--ink);
  }
  .flyer--en { left: 107px; }
  .flyer--fr { left: 487px; }
  .flyer__head { position: absolute; left: 0; top: 0; width: 100%; height: 142px; background: linear-gradient(90deg, #dfe3e6 40%, #f1f4f6 70%, #f6f8fa); }
  .flyer__photo { position: absolute; left: 0; top: 0; width: 165px; height: 142px; background: linear-gradient(120deg, #bfc4c7 0%, #6c7074 40%, #3b3e42 70%, #c9ccce 100%); }
  .flyer__title { position: absolute; font-family: "Anton", Impact, sans-serif; font-weight: 400; line-height: .98; }
  .flyer__title .dark { color: #3c3f45; display: block; }
  .flyer__title .accent { color: var(--teal-text); display: block; }
  .flyer__sub { position: absolute; font-size: 11.5px; line-height: 1.15; color: var(--ink); }
  .flyer__badge { width: 66px; height: 66px; }
  .flyer__badge .badge__price { font-size: 13px; }
  .flyer__badge .badge__line { font-size: 8.5px; }
  .flyer__band { position: absolute; top: 142px; left: 0; width: 100%; height: 27px; background: var(--teal); color: var(--white); text-align: center; font-size: 18px; font-weight: 500; line-height: 28px; }
  .flyer__intro { position: absolute; top: 169px; left: 0; width: 100%; height: 50px; background: var(--mist); text-align: center; display: flex; align-items: center; justify-content: center; line-height: 1.2; padding: 0 14px; }
  .flyer--en .flyer__intro { font-size: 12px; }
  .flyer--fr .flyer__intro { font-size: 9.5px; }

  .plan { position: absolute; left: 61px; right: 10px; }
  .plan__num { position: absolute; left: -39px; top: -6px; width: 30px; height: 30px; border-radius: 50%; background: var(--teal); color: var(--white); font-size: 20px; text-align: center; line-height: 30px; }
  .plan__name { color: var(--teal-text); font-size: 10px; text-transform: uppercase; line-height: 12px; }
  .plan__desc { font-size: 10px; line-height: 12px; }
  .plan__perks { list-style: none; font-size: 10px; line-height: 12px; margin-top: 12px; }
  .plan__perks li { padding-left: 7px; text-indent: -7px; }
  .plan__perks li::before { content: "\2022"; padding-right: 3px; font-size: 8px; }
  .flyer--fr .plan__desc { font-size: 8.3px; line-height: 11px; }
  .flyer--fr .plan__perks { margin-top: 0; line-height: 11.5px; }
  .plan--shift { left: 65px; }

  .flyer__foot { position: absolute; left: 0; width: 100%; background: var(--grey-bg); }
  .flyer--en .flyer__foot { top: 616px; height: 71px; }
  .flyer--fr .flyer__foot { top: 598px; height: 82px; }
  .cta {
    position: absolute; left: 27px; top: 11px; width: 290px; height: 27px; border-radius: 14px;
    background: linear-gradient(#1c6d8a, #0b2f40 70%, #08222e);
    color: var(--white); font-family: "Roboto Condensed", Arial, sans-serif; font-size: 15.5px;
    text-align: center; line-height: 27px; box-shadow: 0 6px 6px -2px rgba(0,0,0,.45);
  }
  .flyer--fr .cta { font-size: 14px; }
</style>
</head>
<body>

<svg class="sprites" aria-hidden="true">
  <symbol id="burst" viewBox="0 0 100 100">
    <polygon points="100,50 91.5,56.6 97.6,65.5 87.4,69.1 90.5,79.4 79.7,79.7 79.4,90.5 69.1,87.4 65.5,97.6 56.6,91.5 50,100 43.4,91.5 34.5,97.6 30.9,87.4 20.6,90.5 20.3,79.7 9.5,79.4 12.6,69.1 2.4,65.5 8.5,56.6 0,50 8.5,43.4 2.4,34.5 12.6,30.9 9.5,20.6 20.3,20.3 20.6,9.5 30.9,12.6 34.5,2.4 43.4,8.5 50,0 56.6,8.5 65.5,2.4 69.1,12.6 79.4,9.5 79.7,20.3 90.5,20.6 87.4,30.9 97.6,34.5 91.5,43.4" fill="#141a4a"/>
  </symbol>
  <symbol id="cursor" viewBox="0 0 9 13">
    <polygon points="0,0 0,11 3,8 5,13 6.5,12.3 4.6,7.6 8.5,7.6" fill="#6ea6dc"/>
  </symbol>
</svg>

<!-- French banner -->
<section class="banner banner--fr">
  <svg class="banner__photo" viewBox="0 0 320 137" role="img" aria-label="Keyboard close-up with a blue Print key">
    <defs>
      <linearGradient id="keysFr" x1="0" y1="0" x2="1" y2="1">
        <stop offset="0" stop-color="#f4f4f4"/><stop offset=".6" stop-color="#d9d9d9"/><stop offset="1" stop-color="#bdbdbd"/>
      </linearGradient>
    </defs>
    <path d="M0 0 H288 Q318 70 258 137 H0 Z" fill="url(#keysFr)"/>
  </svg>
  <div class="badge banner__badge">
    <svg><use href="#burst"/></svg>
    <div class="badge__text"><span class="badge__price">$9.95</span><span class="badge__line">un mois pour</span><span class="badge__line">Terme de</span><span class="badge__line">3 ans</span></div>
  </div>
  <div class="banner__copy">
    <h2 class="banner__title">IMPRIMANTE GRATUITE</h2>
    <p class="banner__sub">Pour un coût mensuel, vous obtenez tout<br>les fournitures et le service inclus</p>
    <div class="pill">5 PLANS DISPONIBLES <svg><use href="#cursor"/></svg></div>
  </div>
</section>

<!-- English banner -->
<section class="banner banner--en">
  <svg class="banner__photo" viewBox="0 0 320 137" role="img" aria-label="Keyboard close-up with a blue Print key">
    <defs>
      <linearGradient id="keysEn" x1="0" y1="0" x2="1" y2="1">
        <stop offset="0" stop-color="#f4f4f4"/><stop offset=".6" stop-color="#d9d9d9"/><stop offset="1" stop-color="#bdbdbd"/>
      </linearGradient>
    </defs>
    <path d="M0 0 H288 Q318 70 258 137 H0 Z" fill="url(#keysEn)"/>
  </svg>
  <div class="badge banner__badge">
    <svg><use href="#burst"/></svg>
    <div class="badge__text"><span class="badge__price">$9.95</span><span class="badge__line">a month for</span><span class="badge__line">3 year term</span></div>
  </div>
  <div class="banner__copy">
    <h2 class="banner__title">FREE PRINTER</h2>
    <p class="banner__sub">For a monthly cost you get all<br>the supplies and service included</p>
    <div class="pill">5 PLANS AVAILABLE <svg><use href="#cursor"/></svg></div>
  </div>
</section>

<!-- English flyer -->
<article class="flyer flyer--en">
  <div class="flyer__head">
    <div class="flyer__photo" role="img" aria-label="Hand pressing buttons on an office multifunction printer"></div>
    <h1 class="flyer__title" style="left:166px; top:34px; font-size:39px;"><span class="dark">FREE</span><span class="accent">PRINTER</span></h1>
    <div class="badge flyer__badge" style="left:268px; top:10px;">
      <svg><use href="#burst"/></svg>
      <div class="badge__text"><span class="badge__price">$9.95</span><span class="badge__line">a month for</span><span class="badge__line">3 year term</span></div>
    </div>
    <p class="flyer__sub" style="left:166px; top:107px;">For a monthly cost you get all<br>the supplies and service included</p>
  </div>
  <div class="flyer__band">5 PLANS AVAILABLE</div>
  <p class="flyer__intro">Prices vary upon printers, most expensive plan is $69.94 a month for a 1 year term and the most affordable plan is $9.95 a month for 3 year term</p>

  <div class="plan" style="top:237px;"><span class="plan__num">1</span><p class="plan__name">Monochrome Laser</p><p class="plan__desc">(print only printer, black and white printing)</p></div>
  <div class="plan" style="top:275px;"><span class="plan__num">2</span><p class="plan__name">Multifunction Monochrome Laser</p><p class="plan__desc">(print scan copy fax printer, black and white printing)</p>
    <ul class="plan__perks"><li>Monochrome Printers are given 1000 prints per month</li><li>Toner included</li><li>Service included</li><li>Printer included</li></ul></div>
  <div class="plan" style="top:369px;"><span class="plan__num">3</span><p class="plan__name">Color Laser</p><p class="plan__desc">(print only printer, color printing)</p></div>
  <div class="plan" style="top:411px;"><span class="plan__num">4</span><p class="plan__name">Multifunction Color Laser</p><p class="plan__desc">(print scan copy fax, color printing)</p>
    <ul class="plan__perks"><li>Color printers are given 500 monochrome prints and 500 color prints per month</li><li>Toner included</li><li>Service included</li><li>Printer included</li></ul></div>
  <div class="plan plan--shift" style="top:519px;"><span class="plan__num">5</span><p class="plan__name">Inkjet Color Printer</p><p class="plan__desc">(print copy scan fax, color printing)</p>
    <ul class="plan__perks"><li>Inkjet Printers are given 1000 prints per month.</li><li>Ink included</li><li>Service included</li><li>Printer included</li></ul></div>

  <div class="flyer__foot"><div class="cta">SUBSCRIPTION SERVICE FOR PRINTING</div></div>
</article>

<!-- French flyer -->
<article class="flyer flyer--fr">
  <div class="flyer__head">
    <div class="flyer__photo" role="img" aria-label="Hand pressing buttons on an office multifunction printer"></div>
    <h1 class="flyer__title" style="left:164px; top:49px;"><span class="dark" style="font-size:21px;">IMPRIMANTE</span><span class="accent" style="font-size:32px;">GRATUITE</span></h1>
    <div class="badge flyer__badge" style="left:267px; top:9px;">
      <svg><use href="#burst"/></svg>
      <div class="badge__text"><span class="badge__price">$9.95</span><span class="badge__line">un mois pour</span><span class="badge__line">Terme de</span><span class="badge__line">3 ans</span></div>
    </div>
    <p class="flyer__sub" style="left:164px; top:107px; font-size:10px;">Pour un coût mensuel, vous obtenez<br>tout les fournitures et le service inclus</p>
  </div>
  <div class="flyer__band">5 PLANS DISPONIBLES</div>
  <p class="flyer__intro">Les prix varient selon les imprimantes, le plan le plus cher est 69,94 $ par mois pour un terme d'un an et le plus abordable le plan est de 9,95 $ par mois pour un terme de 3 ans</p>

  <div class="plan" style="top:237px;"><span class="plan__num">1</span><p class="plan__name">Laser Monochrome</p><p class="plan__desc">(impression uniquement imprimante, impression noir et blanc)</p></div>
  <div class="plan" style="top:275px;"><span class="plan__num">2</span><p class="plan__name">Laser Monochrome Multifonction</p><p class="plan__desc">(impression numérisation copie fax imprimante, impression noir et blanc)</p>
    <ul class="plan__perks"><li>Les imprimantes monochromes reçoivent 1 000 impressions par mois</li><li>Toner inclus</li><li>Service inclus</li><li>Imprimante incluse</li></ul></div>
  <div class="plan" style="top:369px;"><span class="plan__num">3</span><p class="plan__name">Laser Couleur</p><p class="plan__desc">(impression uniquement imprimante, impression couleur)</p></div>
  <div class="plan" style="top:411px;"><span class="plan__num">4</span><p class="plan__name">Laser Couleur Multifonction</p><p class="plan__desc">(impression numérisation copie fax, impression couleur)</p>
    <ul class="plan__perks"><li>Les imprimantes couleur reçoivent 500 impressions monochromes et 500 impressions couleur par mois</li><li>Toner inclus</li><li>Service inclus</li><li>Imprimante incluse</li></ul></div>
  <div class="plan plan--shift" style="top:509px;"><span class="plan__num">5</span><p class="plan__name">Imprimante couleur à jet d'encre</p><p class="plan__desc">(impression copie numérisation fax, impression couleur)</p>
    <ul class="plan__perks"><li>Les imprimantes à jet d'encre reçoivent 1 000 impressions par mois.</li><li>Encre incluse</li><li>Service inclus</li><li>Imprimante incluse</li></ul></div>

  <div class="flyer__foot"><div class="cta">SERVICE D'ABONNEMENT POUR L'IMPRESSION</div></div>
</article>

</body>
</html>
```